Business Card and Letterhead for Vantage Psychology

We need a business card design and letterhead to use for our Psychology firm that specializes in psychoeducational assessments and individual therapy. Our motto is Purpose-Driven Assessments, Meaning-Centered Therapy.Our contact information is as follows:
Vantage Psychology
The Marwick Block - 6127-48St.
Box 2716 Olds, AB
T2K 3M8
t 403.555.0148 (VANT)
f 403.555.0172
www.vantagepsychology-example.ca
The business card will be used for two different psychologists so I can supply names nearer to completion. We prefer clean, uncluttered looks.

Target Market(s)

Clients, Educators

Font styles to use
Sans Serif

Colors

Designer to choose colors to be used in the design.

Requirements
Must have
• All relevant contact info, logo, some "white" space.
Nice to have
• It would be nice to see letterhead options that have the logo on the top of the page but also options that have it on the side. I think top of the page is probably our preference.
Should not have
• Too much clutter!

```html
<!DOCTYPE html>
<html lang="en">
<head>
<meta charset="utf-8">
<title>Vantage Psychology – Stationery</title>
<link href="https://fonts.googleapis.com/css2?family=Montserrat:wght@300;400;500&family=Lato:wght@700&display=swap" rel="stylesheet">
<style>
  :root {
    --sky: #56bddb;
    --amber: #f2a847;
    --ink: #2a2a2a;
    --text: #3a3a3a;
    --paper: #ffffff;
    --backdrop: #e8e8e8;
    --rule: #8a8a8a;
  }
  * { margin: 0; padding: 0; box-sizing: border-box; }
  html, body { width: 1200px; height: 1200px; overflow: hidden; }
  body { background: var(--backdrop); position: relative; font-family: "Montserrat", sans-serif; color: var(--text); }

  .sheet, .card { position: absolute; background: var(--paper); overflow: hidden; box-shadow: 8px 10px 14px rgba(0,0,0,.35); }
  .swoosh { position: absolute; left: 0; top: 0; width: 100%; height: 100%; }

  /* Letterhead */
  .letterhead { left: 268px; top: 169px; width: 667px; height: 864px; }
  .letterhead__emblem { position: absolute; left: 304px; top: 62px; }
  .brand-dot { display: block; border-radius: 50%; background: var(--sky); }
  .letterhead .brand-dot { width: 60px; height: 60px; }
  .letterhead__masthead { position: absolute; left: 0; right: 0; top: 130px; display: flex; align-items: center; gap: 10px; }
  .letterhead__rule { flex: 1; height: 1px; background: var(--rule); }
  .brand-name { font-family: "Montserrat", sans-serif; font-weight: 500; color: var(--amber); letter-spacing: .05em; text-transform: uppercase; white-space: nowrap; }
  .letterhead .brand-name { font-size: 15px; line-height: 18px; }
  .letterhead__footer { position: absolute; left: 0; right: 0; top: 807px; color: #fff; font-weight: 300; font-size: 12px; letter-spacing: .04em; text-align: center; }
  .letterhead__address { padding-bottom: 4px; margin: 0 auto; width: 380px; border-bottom: 1px solid rgba(255,255,255,.5); }
  .letterhead__contacts { margin-top: 6px; display: flex; justify-content: center; gap: 20px; }
  .contact-item { display: inline-flex; align-items: center; gap: 4px; }
  .contact-item svg { width: 8px; height: 8px; fill: currentColor; }

  /* Business card front */
  .card { width: 350px; height: 200px; top: 358px; }
  .card--front { left: 92px; }
  .card__brand { position: absolute; left: 12px; width: 170px; top: 70px; display: flex; flex-direction: column; align-items: center; gap: 9px; }
  .card--front .brand-dot { width: 46px; height: 46px; }
  .card--front .brand-name { font-size: 10.5px; }
  .card__divider { position: absolute; left: 190px; top: 48px; width: 1px; height: 100px; background: #9a9a9a; }
  .card__details { position: absolute; left: 200px; top: 46px; font-size: 6.5px; line-height: 1.6; white-space: nowrap; letter-spacing: -.01em; }
  .card__name { font-family: "Lato", sans-serif; font-weight: 700; color: var(--sky); font-size: 11px; line-height: 1.2; letter-spacing: 0; }
  .card__block { margin-top: 7px; }
  .card__line { display: flex; align-items: center; gap: 6px; }
  .card__line svg { width: 6px; height: 6px; fill: var(--amber); flex: none; }

  /* Business card back */
  .card--back { left: 781px; background: var(--ink); }
  .card--back .brand-dot { position: absolute; left: 120px; top: 48px; width: 110px; height: 110px; }
  .card--back .brand-name { position: absolute; left: 0; right: 0; top: 176px; text-align: center; color: #fff; font-size: 11.5px; }
</style>
</head>
<body>

<section class="sheet letterhead" aria-label="Letterhead">
  <svg class="swoosh" viewBox="0 0 667 864" preserveAspectRatio="none" aria-hidden="true">
    <path d="M24 769 Q333 722 643 769 Q333 741 24 769 Z" fill="var(--sky)"/>
    <path d="M0 795 Q333 749 667 795 L667 864 L0 864 Z" fill="var(--amber)"/>
  </svg>
  <div class="letterhead__emblem"><span class="brand-dot"></span></div>
  <div class="letterhead__masthead">
    <span class="letterhead__rule"></span>
    <span class="brand-name">Vantage Psychology</span>
    <span class="letterhead__rule"></span>
  </div>
  <footer class="letterhead__footer">
    <p class="letterhead__address">The Marwick Block - 6127-48St., Box 2716 Olds AB T2K 3M8</p>
    <p class="letterhead__contacts">
      <span class="contact-item"><svg viewBox="0 0 10 10"><path d="M2 0.5 L3.8 2.6 L2.9 3.8 Q4 6 6.2 7.1 L7.4 6.2 L9.5 8 L8.3 9.5 Q3.5 9 0.5 1.7 Z"/></svg>403.555.0148 (VANT)</span>
      <span class="contact-item"><svg viewBox="0 0 10 10"><path d="M2.5 0.5h5v2.5h-5z M0.5 3.5h9v4h-9z M2.5 6.5h5v3h-5z"/></svg>403.555.0172</span>
      <span class="contact-item"><svg viewBox="0 0 10 10"><circle cx="5" cy="5" r="4.5"/></svg>www.vantagepsychology-example.ca</span>
    </p>
  </footer>
</section>

<section class="card card--front" aria-label="Business card front">
  <svg class="swoosh" viewBox="0 0 350 200" preserveAspectRatio="none" aria-hidden="true">
    <path d="M14 187 Q175 159 336 187 Q175 169 14 187 Z" fill="var(--sky)"/>
    <path d="M0 195 Q175 172 350 195 L350 200 L0 200 Z" fill="var(--amber)"/>
  </svg>
  <div class="card__brand">
    <span class="brand-dot"></span>
    <span class="brand-name">Vantage Psychology</span>
  </div>
  <span class="card__divider"></span>
  <div class="card__details">
    <p class="card__name">Delia Harcourt-Vance</p>
    <p>M.Ed., R.Psych.</p>
    <p class="card__block">6127-48St., Box 2716<br>Olds AB T2K 3M8</p>
    <div class="card__block">
      <p class="card__line"><svg viewBox="0 0 10 10"><path d="M2 0.5 L3.8 2.6 L2.9 3.8 Q4 6 6.2 7.1 L7.4 6.2 L9.5 8 L8.3 9.5 Q3.5 9 0.5 1.7 Z"/></svg>403.555.0148 (VANT)</p>
      <p class="card__line"><svg viewBox="0 0 10 10"><path d="M2.5 0.5h5v2.5h-5z M0.5 3.5h9v4h-9z M2.5 6.5h5v3h-5z"/></svg>403.555.0172</p>
      <p class="card__line"><svg viewBox="0 0 10 10"><path d="M0.5 1.5h9v7h-9z M0.5 1.5 L5 5.5 L9.5 1.5" fill="none" stroke="var(--amber)" stroke-width="1"/></svg>delia@vantagepsychology-example.ca</p>
      <p class="card__line"><svg viewBox="0 0 10 10"><circle cx="5" cy="5" r="4.5"/></svg>www.vantagepsychology-example.ca</p>
    </div>
  </div>
</section>

<section class="card card--back" aria-label="Business card back">
  <svg class="swoosh" viewBox="0 0 350 200" preserveAspectRatio="none" aria-hidden="true">
    <path d="M12 173 Q175 145 338 173 Q175 156 12 173 Z" fill="var(--sky)"/>
    <path d="M0 175 Q175 155 350 175 L350 200 L0 200 Z" fill="var(--amber)"/>
  </svg>
  <span class="brand-dot"></span>
  <span class="brand-name">Vantage Psychology</span>
</section>

</body>
</html>
```